Vex Lira

Hello - our company Orbana 9 develops novel products for the skin, & hair care industry as well as dietary supplements. We're looking for a label design for a new product. The product is a premium hair loss/growth supplement. Our primary demo is women ages 45-65. I attached the brand logo & some competitive product designs that we find attractive.

I've been traveling & have not had the time to adequately review the designs, please be patient with me.

```html
<!DOCTYPE html>
<html lang="en">
<head>
<meta charset="utf-8">
<title>Orbana 9 — Vex Lira Hair Supplement Label</title>
<link rel="stylesheet" href="https://fonts.googleapis.com/css2?family=Open+Sans:wght@400;700&family=Bitter:wght@300;400&family=Oswald:wght@500;700&display=swap">
<style>
  :root {
    --page: #ffffff;
    --label-black: #0d0d0e;
    --label-charcoal: #1c1c1f;
    --gold-dark: #8a5a1c;
    --gold-mid: #c8923e;
    --gold-light: #f4d785;
    --accent-blue: #3fa9dc;
    --text-white: #f5f5f5;
    --text-grey: #8d8f93;
  }
  * { margin: 0; padding: 0; box-sizing: border-box; }
  html, body {
    width: 1200px;
    height: 1200px;
    overflow: hidden;
    background: var(--page);
  }
  .label {
    position: absolute;
    left: 185px;
    top: 60px;
    width: 830px;
    height: 1080px;
    background: radial-gradient(ellipse at 50% 25%, var(--label-charcoal) 0%, var(--label-black) 70%);
    overflow: hidden;
  }
  .gold-band {
    position: absolute;
    left: 0;
    width: 100%;
    height: 47px;
    background: linear-gradient(90deg, var(--gold-dark) 0%, var(--gold-mid) 20%, var(--gold-light) 50%, var(--gold-mid) 80%, var(--gold-dark) 100%);
  }
  .gold-band--top { top: 0; }
  .gold-band--bottom { bottom: 0; }
  .gold-rule {
    position: absolute;
    left: 0;
    width: 100%;
    height: 3px;
    background: linear-gradient(90deg, var(--gold-dark), var(--gold-light), var(--gold-dark));
  }
  .gold-rule--top { top: 54px; }
  .gold-rule--bottom { top: 1020px; }

  .centered {
    position: absolute;
    left: 0;
    width: 100%;
    text-align: center;
    white-space: nowrap;
  }
  .product-name {
    top: 92px;
    font-family: "Open Sans", sans-serif;
    font-weight: 700;
    font-size: 92px;
    line-height: 1;
    color: var(--text-white);
    letter-spacing: -1px;
  }
  .claim {
    top: 200px;
    font-family: "Bitter", serif;
    font-weight: 300;
    font-size: 47px;
    line-height: 1;
    color: var(--accent-blue);
  }
  .ingredient {
    top: 258px;
    font-family: "Bitter", serif;
    font-weight: 300;
    font-size: 37px;
    line-height: 1;
    color: var(--text-white);
  }
  .brand-name {
    top: 378px;
    font-family: "Open Sans", sans-serif;
    font-weight: 400;
    font-size: 96px;
    line-height: 1;
    color: var(--accent-blue);
    letter-spacing: 4px;
  }
  .strength {
    top: 474px;
    font-family: "Bitter", serif;
    font-weight: 300;
    font-size: 46px;
    line-height: 1;
    color: var(--text-white);
    letter-spacing: 2px;
  }
  .growth-badge {
    position: absolute;
    left: 320px;
    top: 605px;
    width: 190px;
    height: 190px;
    border-radius: 50%;
    border: 6px solid var(--gold-mid);
    background: radial-gradient(circle, #ffffff 0%, #e9e9e9 100%);
  }
  .growth-caption {
    top: 806px;
    font-family: "Oswald", sans-serif;
    font-weight: 700;
    font-size: 30px;
    line-height: 1;
    color: var(--text-white);
    letter-spacing: 2px;
  }
  .formula {
    top: 905px;
    font-family: "Bitter", serif;
    font-weight: 300;
    font-size: 50px;
    line-height: 1.05;
    color: var(--text-white);
  }
  .count-seal {
    position: absolute;
    left: 691px;
    top: 882px;
    width: 82px;
    height: 82px;
  }
  .count-unit {
    position: absolute;
    left: 652px;
    top: 972px;
    width: 160px;
    text-align: center;
    font-family: "Oswald", sans-serif;
    font-weight: 500;
    font-size: 26px;
    line-height: 1;
    color: var(--text-grey);
  }
</style>
</head>
<body>
  <main class="label">
    <div class="gold-band gold-band--top"></div>
    <div class="gold-rule gold-rule--top"></div>

    <h1 class="centered product-name">Orbana 9</h1>
    <p class="centered claim">Medically Proven</p>
    <p class="centered ingredient">He Shou Wu 12:1 Extract</p>

    <p class="centered brand-name">Vex Lira</p>
    <p class="centered strength">CLINICAL STRENGTH</p>

    <div class="growth-badge" role="img" aria-label="Hair follicle growth illustration"></div>
    <p class="centered growth-caption">PREMIUM HAIR GROWTH</p>

    <p class="centered formula">Advance Formula<br>Women</p>

    <svg class="count-seal" viewBox="0 0 82 82" aria-label="60">
      <defs>
        <linearGradient id="seal-gold" x1="0" y1="0" x2="1" y2="1">
          <stop offset="0" stop-color="#f4d785"/>
          <stop offset="0.5" stop-color="#c8923e"/>
          <stop offset="1" stop-color="#8a5a1c"/>
        </linearGradient>
      </defs>
      <circle cx="41" cy="41" r="39" fill="url(#seal-gold)"/>
      <circle cx="41" cy="41" r="31" fill="#fff3dc" stroke="#8a5a1c" stroke-width="2"/>
      <text x="41" y="54" text-anchor="middle" font-family="Oswald, sans-serif" font-weight="700" font-size="36" fill="#b07a2e">60</text>
    </svg>
    <p class="count-unit">CAPSULES</p>

    <div class="gold-rule gold-rule--bottom"></div>
    <div class="gold-band gold-band--bottom"></div>
  </main>
</body>
</html>
```